"Breathe & Bloom" Book Cover 5.5x8.5

Title of the book is "Breathe & Bloom"
Subtitle is "Unmasking Pricing Myths"
I've used PixelGuild on multiple occasions you can look on my Borvex page, Mark Delwitt, to see the covers I've used in the other projects I've done.
The target audience are people who have been tricked to think they can't retire because inflation, i.e. cost of living is going up so much they must work to keep up. There is no evidence of this.
And those are the people I want to reach so they can "Breathe...and Bloom."
Target Market(s)
Americans aged 55 and over who are thinking about retirement
Industry/Entity Type
Financial
Requirements
Nice to have
- Keep It Simple, Stupid is my mantra. Just make it pop out when people are browsing
Should not have
- No piggy banks. No old people sitting on a beach.

```html
<!DOCTYPE html>
<html lang="en">
<head>
<meta charset="utf-8">
<title>Breathe &amp; Bloom — Book Cover</title>
<link href="https://fonts.googleapis.com/css2?family=Barlow:wght@600;700&family=Barlow+Semi+Condensed:wght@600&display=swap" rel="stylesheet">
<style>
  :root {
    --purple: #663a82;
    --stone: #736a5c;
    --paper: #fbfbf8;
    --white: #ffffff;
    --skin-light: #f6e6da;
    --skin-mid: #e8c7b1;
    --note-light: #e6dfc9;
    --note-dark: #a9a48c;
    --pin: #9a9a94;
  }
  html, body {
    margin: 0;
    padding: 0;
    overflow: hidden;
    background: var(--paper);
  }
  .cover {
    position: relative;
    width: 776px;
    height: 1200px;
    background: var(--paper);
    overflow: hidden;
  }
  .title-art {
    position: absolute;
    left: 0;
    top: 0;
  }
  .title-word {
    font-family: "Barlow Semi Condensed", "Barlow", sans-serif;
    font-weight: 600;
    fill: var(--purple);
  }
  .subtitle {
    position: absolute;
    left: 55px;
    top: 606px;
    margin: 0;
    font-family: "Barlow", sans-serif;
    font-weight: 700;
    font-size: 64px;
    line-height: 68px;
    letter-spacing: 2px;
    color: var(--stone);
    text-transform: uppercase;
  }
  .hand-photo {
    position: absolute;
    left: 474px;
    top: 530px;
    width: 302px;
    height: 248px;
    border-radius: 90px 0 70px 110px;
    background: linear-gradient(200deg, var(--skin-light), var(--skin-mid));
  }
  .pin-photo {
    position: absolute;
    left: 486px;
    top: 768px;
    width: 2px;
    height: 116px;
    background: linear-gradient(var(--pin), #d8d8d4);
    transform: rotate(35deg);
    transform-origin: top center;
  }
  .band {
    position: absolute;
    left: 0;
    top: 1006px;
    width: 776px;
    height: 194px;
    background: var(--purple);
  }
  .banknote-photo {
    position: absolute;
    left: 52px;
    top: 880px;
    width: 650px;
    height: 230px;
    border-radius: 30px 18px 40px 22px;
    transform: skewY(10deg);
    background: linear-gradient(160deg, var(--note-light), var(--note-dark));
  }
  .author {
    position: absolute;
    left: 45px;
    top: 1124px;
    margin: 0;
    font-family: "Barlow", sans-serif;
    font-weight: 700;
    font-size: 46px;
    line-height: 46px;
    letter-spacing: 1px;
    color: var(--white);
    text-transform: uppercase;
  }
</style>
</head>
<body>
<main class="cover">
  <svg class="title-art" width="776" height="520" viewBox="0 0 776 520" aria-label="Breathe and Bloom">
    <text class="title-word" x="55" y="213" font-size="212" textLength="666" lengthAdjust="spacingAndGlyphs">BREATHE</text>
    <rect x="63" y="286" width="167" height="17" fill="var(--purple)"/>
    <rect x="555" y="286" width="166" height="17" fill="var(--purple)"/>
    <text class="title-word" x="243" y="343" font-size="144" textLength="296" lengthAdjust="spacingAndGlyphs">AND</text>
    <text class="title-word" x="55" y="511" font-size="212" textLength="676" lengthAdjust="spacingAndGlyphs">BLOOM</text>
  </svg>

  <h2 class="subtitle">Unmasking<br>Pricing<br>Myths</h2>

  <div class="hand-photo" role="img" aria-label="Photo of a hand holding a pin, about to prick the banknote"></div>
  <div class="pin-photo" role="img" aria-label="Thin pin pointing at the inflated banknote"></div>

  <div class="band"></div>
  <div class="banknote-photo" role="img" aria-label="Photo of an inflated one-dollar banknote"></div>

  <p class="author">Mark Delwitt</p>
</main>
</body>
</html>
```